Velkano Holdings Ltd - An invesmtent & trading company needs a web design

We need a web design for our company based in Cyprus. The company was founded in 2009. We have continuously grown and now invest & trade all over the world.

Velkano Holdings ltd. specializes in the buying and selling of crude oil, precious metals and the investment in properties.

We know that trust is of the utmost importance when it comes to business and the design should communicate this to prospective business partners. Find attached the company logo. The colour scheme for the website should use similar colours and ideally incorporate the logo in some shape or form as well.

Target Market(s)

Oil Traders, Metall Traders, Property Investments

Industry/Entity Type

Trade

Coding

Coded - Design and coding required

Number of Pages Required

4 page

Font styles to use
Sans Serif

Requirements
Must have
• Mainpage,
• About Us
• Partners
• Legal Notice

```html
<!DOCTYPE html>
<html lang="en">
<head>
<meta charset="utf-8">
<title>Velkano Holdings Ltd</title>
<link rel="stylesheet" href="https://fonts.googleapis.com/css2?family=Open+Sans:wght@400;600;700&display=swap">
<style>
:root{
  --navy:#1d3f73;
  --navy-dark:#17305a;
  --cyan:#29b6de;
  --cyan-dark:#1f9fc4;
  --text:#444b55;
  --muted:#8a9099;
  --white:#ffffff;
  --light:#f4f5f7;
}
*{box-sizing:border-box;margin:0;padding:0}
html,body{width:874px;height:1200px;overflow:hidden}
body{font-family:"Open Sans",Arial,sans-serif;color:var(--text);background:var(--white)}
.page{width:874px;height:1200px;position:relative}

.site-header{height:80px;display:flex;align-items:center;justify-content:space-between;padding:0 120px}
.brand{display:flex;align-items:center;gap:10px}
.brand-mark{width:30px;height:30px;background:var(--navy);flex:none}
.brand-name{font-weight:700;font-size:15px;color:var(--navy);letter-spacing:.3px;white-space:nowrap}
.main-nav{display:flex;gap:20px}
.main-nav a{font-size:10.5px;font-weight:600;color:var(--navy);text-decoration:none;padding-bottom:4px}
.main-nav a.active{color:var(--cyan);border-bottom:2px solid var(--cyan)}

.hero{height:357px;position:relative;background:linear-gradient(180deg,#5f8fc4 0%,#93b8dd 45%,#c9d9e8 70%,#7f8a86 100%)}
.hero-caption{position:absolute;left:364px;top:196px;width:437px;background:rgba(20,60,110,.85);color:var(--white);text-align:center;padding:12px 20px 14px}
.hero-caption h1{font-size:25px;font-weight:600;margin-bottom:4px;white-space:nowrap}
.hero-caption p{font-size:10px;line-height:1.4;opacity:.9}

.about{height:218px;text-align:center;padding:52px 120px 0}
.about h2{font-size:23px;font-weight:600;color:var(--navy);margin-bottom:6px}
.about .rule{width:520px;height:1px;background:#d6dae0;margin:0 auto 14px}
.about p{font-size:8.5px;line-height:1.55;color:var(--muted);margin-bottom:8px}

.services{height:291px;background:var(--cyan);position:relative;padding-top:48px;overflow:hidden}
.section-tab{position:absolute;top:0;left:50%;transform:translateX(-50%);background:var(--navy);color:var(--white);font-size:14px;font-weight:600;padding:7px 32px 8px;white-space:nowrap}
.service-list{display:flex;justify-content:center;gap:50px}
.service{width:190px;text-align:center;color:var(--white)}
.service-photo{width:112px;height:112px;border-radius:50%;border:4px solid var(--white);margin:0 auto 8px}
.photo-oil{background:radial-gradient(circle,#8d6a3c,#3b2b1c)}
.photo-metal{background:radial-gradient(circle,#e3c779,#8e6e2b)}
.photo-property{background:linear-gradient(180deg,#7fb3dd,#c4b08c 60%,#6a6a5e)}
.service h3{font-size:16px;font-weight:600;margin-bottom:3px;white-space:nowrap}
.service p{font-size:7.5px;line-height:1.5;opacity:.95;margin-bottom:9px;padding:0 8px;height:34px}
.btn{display:inline-block;border:1px solid var(--white);color:var(--white);font-size:9px;padding:4px 12px;text-decoration:none}

.partners{height:160px;text-align:center;padding-top:26px}
.partners h2{font-size:19px;font-weight:400;color:var(--muted);margin-bottom:6px}
.partners .rule{width:400px;height:1px;background:#e1e4e8;margin:0 auto 30px}
.partner-row{display:flex;justify-content:center;align-items:center;gap:40px}
.partner-badge{width:78px;height:22px;background:#c8ccd2;border-radius:3px}

.site-footer{height:94px;background:var(--navy);color:var(--white);padding:24px 120px 0}
.footer-top{display:flex;justify-content:space-between;align-items:center;margin-bottom:12px}
.footer-nav{display:flex;gap:6px;font-size:9.5px;font-weight:600}
.footer-nav a{color:var(--white);text-decoration:none}
.footer-nav span{opacity:.6}
.social{display:flex;gap:6px}
.social span{width:18px;height:18px;border-radius:50%;background:var(--cyan)}
.copyright{font-size:8px;opacity:.7}
</style>
</head>
<body>
<div class="page">
  <header class="site-header">
    <div class="brand">
      <span class="brand-mark"></span>
      <span class="brand-name">VELKANO HOLDINGS LTD</span>
    </div>
    <nav class="main-nav">
      <a class="active" href="#">HOME</a>
      <a href="#">ABOUT US</a>
      <a href="#">PARTNER</a>
      <a href="#">LEGAL NOTICE</a>
      <a href="#">CONTACT US</a>
    </nav>
  </header>

  <section class="hero" role="img" aria-label="Oil pump jacks at an oil field under a blue sky">
    <div class="hero-caption">
      <h1>Buying and Selling of Crude Oil</h1>
      <p>Trusted partners in global commodity trading since 2009, delivering secure and transparent deals worldwide</p>
    </div>
  </section>

  <section class="about">
    <h2>ABOUT VELKANO HOLDINGS LTD</h2>
    <div class="rule"></div>
    <p>Velkano Holdings Ltd is an investment and trading company based in Cyprus. Founded in 2009, we have grown steadily and now invest and trade across the world. Our team builds long lasting relationships with partners who value reliability, discretion and fair terms in every transaction we undertake together.</p>
    <p>We specialise in crude oil, precious metals and property investment, guided by trust and careful risk management.</p>
  </section>

  <section class="services">
    <div class="section-tab">We Specialised In</div>
    <div class="service-list">
      <article class="service">
        <div class="service-photo photo-oil" role="img" aria-label="Stacked crude oil barrels"></div>
        <h3>Crude Oil</h3>
        <p>Physical crude oil trading with reliable sourcing, secure logistics and clear contracts for buyers worldwide.</p>
        <a class="btn" href="#">Click here</a>
      </article>
      <article class="service">
        <div class="service-photo photo-metal" role="img" aria-label="Pile of precious metal nuggets"></div>
        <h3>Precious Metals</h3>
        <p>Buying and selling of gold, silver and platinum with verified origin and insured storage and delivery.</p>
        <a class="btn" href="#">Click here</a>
      </article>
      <article class="service">
        <div class="service-photo photo-property" role="img" aria-label="Residential building exterior"></div>
        <h3>Investment Properties</h3>
        <p>Long term investment in residential and commercial properties selected for stable value and steady returns.</p>
        <a class="btn" href="#">Click here</a>
      </article>
    </div>
  </section>

  <section class="partners">
    <h2>Our Partners</h2>
    <div class="rule"></div>
    <div class="partner-row">
      <span class="partner-badge"></span>
      <span class="partner-badge"></span>
      <span class="partner-badge"></span>
      <span class="partner-badge"></span>
      <span class="partner-badge"></span>
      <span class="partner-badge"></span>
    </div>
  </section>

  <footer class="site-footer">
    <div class="footer-top">
      <nav class="footer-nav">
        <a href="#">HOME</a><span>|</span>
        <a href="#">ABOUT US</a><span>|</span>
        <a href="#">PARTNERS</a><span>|</span>
        <a href="#">LEGAL NOTICE</a><span>|</span>
        <a href="#">CONTACT US</a>
      </nav>
      <div class="social"><span></span><span></span><span></span><span></span></div>
    </div>
    <p class="copyright">© 2024 Velkano Holdings Ltd. All rights reserved.</p>
  </footer>
</div>
</body>
</html>
```